Business Card Design using new logo

As much as we'd like to think that treating everyone equally is the best strategy for fairness, the reality is that the differences in the lives of women and men have to be taken into account to ensure that organizations, programs, services, and yes, even public policy treat women and men in ways that achieve gender equity.

That's where ParityLoom - balance insight metrics comes in. Using the data-driven tools of gender analysis, our organization can help anyone determine if gender equity is being achieved - in businesses and organizations, in the planning and implementation of programs and services, and in the development and enforcement of public policy.
Updates

Apologies for the delay - have not had time to finalize the decision.  Should be early this week - probably Tuesday.

Industry/Entity Type

Business

Requirements
Must have
• New Logo for ParityLoom
• Logo plus words "Balance Insight Metrics"

```html
<!DOCTYPE html>
<html lang="en">
<head>
<meta charset="utf-8">
<title>ParityLoom – Business Cards</title>
<link href="https://fonts.googleapis.com/css2?family=Arimo:wght@400;700&display=swap" rel="stylesheet">
<style>
  :root {
    --backdrop: #d9dadc;
    --card-dark: #2f2f31;
    --card-light: #ffffff;
    --brand-orange: #f39a1e;
    --brand-grey: #b9b9bb;
    --ink: #222222;
    --rule: #9a9a9a;
  }
  html, body {
    margin: 0;
    padding: 0;
    width: 1200px;
    height: 900px;
    overflow: hidden;
    background: var(--backdrop);
    font-family: "Arimo", Arial, sans-serif;
  }
  .canvas {
    position: relative;
    width: 1200px;
    height: 900px;
  }
  .card {
    position: absolute;
    width: 540px;
    height: 310px;
    border-radius: 26px;
    overflow: hidden;
    box-shadow: 0 6px 18px rgba(0,0,0,0.18);
  }

  /* Back of card */
  .card--back {
    left: 600px;
    top: 120px;
    background: var(--card-dark);
  }
  .card--back .brand {
    position: absolute;
    left: 0;
    right: 0;
    top: 96px;
    text-align: center;
  }
  .brand-mark {
    display: inline-flex;
    align-items: center;
    gap: 14px;
  }
  .brand-dot {
    width: 40px;
    height: 40px;
    border-radius: 50%;
    background: var(--brand-orange);
  }
  .card--back .brand-name {
    font-size: 54px;
    font-weight: 400;
    color: var(--brand-grey);
    letter-spacing: 0.5px;
  }
  .card--back .brand-tagline {
    margin-top: 4px;
    font-size: 17px;
    color: var(--brand-orange);
    letter-spacing: 0.4px;
  }
  .card--back .base-rule {
    position: absolute;
    left: 0;
    right: 0;
    top: 252px;
    height: 6px;
    background: var(--brand-grey);
  }

  /* Front of card */
  .card--front {
    left: 60px;
    top: 470px;
    background: var(--card-light);
  }
  .card--front .brand {
    position: absolute;
    left: 36px;
    top: 34px;
  }
  .card--front .brand-dot {
    width: 30px;
    height: 30px;
  }
  .card--front .brand-name {
    font-size: 38px;
    font-weight: 400;
    color: var(--ink);
  }
  .person {
    position: absolute;
    left: 40px;
    top: 102px;
    color: var(--ink);
    font-size: 13px;
    line-height: 1.3;
  }
  .person-name {
    font-size: 18px;
    color: var(--brand-orange);
  }
  .person-role { margin-bottom: 14px; }
  .label { color: var(--brand-orange); }
  .office {
    position: absolute;
    left: 340px;
    top: 96px;
    padding-left: 16px;
    border-left: 1px solid var(--rule);
    font-size: 13px;
    line-height: 1.3;
    color: var(--ink);
  }
  .office-web { color: var(--brand-orange); }
  .front-graphics {
    position: absolute;
    inset: 0;
  }
</style>
</head>
<body>
<main class="canvas">

  <section class="card card--back" aria-label="Card back">
    <div class="brand">
      <div class="brand-mark">
        <span class="brand-dot"></span>
        <span class="brand-name">ParityLoom</span>
      </div>
      <div class="brand-tagline">Balance Insight Metrics</div>
    </div>
    <div class="base-rule"></div>
  </section>

  <section class="card card--front" aria-label="Card front">
    <svg class="front-graphics" width="540" height="310" viewBox="0 0 540 310">
      <polygon points="0,280 492,192 494,204 0,296" fill="#f39a1e"/>
      <polygon points="520,193 486,178 496,220" fill="#f39a1e"/>
    </svg>

    <div class="brand">
      <div class="brand-mark">
        <span class="brand-dot"></span>
        <span class="brand-name">ParityLoom</span>
      </div>
    </div>

    <div class="person">
      <div class="person-name">Maren Holloway II</div>
      <div class="person-role">General Manager</div>
      <div>Balance Insight Metrics LLC</div>
      <div><span class="label">C:</span> + 00 98 765 4321</div>
      <div><span class="label">E:</span> maren@parityloom.com</div>
    </div>

    <div class="office">
      <div><span class="label">P:</span> + 00 98 765 4321</div>
      <div><span class="label">F:</span> + 00 98 765 4321</div>
      <div class="office-web">www.parityloom.com</div>
    </div>
  </section>

</main>
</body>
</html>
```